HarmoNest Ensemble Jubilee
Date: Sunday Oct 2, 2022
When: 2-4 p.m.
Location: Brindle9 Alehouse
413 Marlowe Ct #200, Sacramento, CA 95821
Tickets: www.Tixolvo.com
General seating: $15 for adults and $10 for students

```html
<!DOCTYPE html>
<html lang="en">
<head>
<meta charset="utf-8">
<title>HarmoNest Ensemble Jubilee</title>
<link rel="stylesheet" href="https://fonts.googleapis.com/css2?family=Monoton&family=Oswald:wght@500;700&family=Poppins:wght@400;600&display=swap">
<style>
  :root {
    --orange: #ef5533;
    --ink: #0f0f0f;
    --panel: #161616;
    --border-band: #1d1d1d;
    --white: #ffffff;
  }
  html, body {
    margin: 0;
    padding: 0;
    width: 960px;
    height: 1200px;
    overflow: hidden;
    background: var(--ink);
  }
  .poster {
    position: relative;
    width: 960px;
    height: 1200px;
    background: var(--ink);
    overflow: hidden;
    text-align: center;
    color: var(--white);
  }
  .notation-frame {
    position: absolute;
    inset: 0;
    border: 26px solid var(--border-band);
    box-sizing: border-box;
    pointer-events: none;
  }
  .stage-backdrop {
    position: absolute;
    inset: 26px;
    background: linear-gradient(160deg, #1a1a1a 0%, #121212 45%, #0d0d0d 100%);
  }
  .content {
    position: relative;
    z-index: 2;
  }
  .brand {
    position: absolute;
    top: 78px;
    left: 0;
    right: 0;
    font-family: "Poppins", sans-serif;
    font-weight: 600;
    font-size: 50px;
    line-height: 1;
    color: var(--orange);
    letter-spacing: -0.5px;
  }
  .title {
    position: absolute;
    top: 186px;
    left: 0;
    right: 0;
    margin: 0;
    font-family: "Monoton", sans-serif;
    font-weight: 400;
    line-height: 1;
    text-transform: uppercase;
  }
  .title span { display: block; }
  .title .line-1 { font-size: 74px; margin-bottom: 18px; }
  .title .line-2 { font-size: 80px; margin-bottom: 18px; }
  .title .line-3 { font-size: 90px; }
  .date-bar {
    position: absolute;
    top: 517px;
    left: 142px;
    width: 684px;
    height: 48px;
    background: var(--orange);
    font-family: "Oswald", sans-serif;
    font-weight: 500;
    font-size: 34px;
    line-height: 48px;
    text-transform: uppercase;
    letter-spacing: 0.3px;
  }
  .venue {
    position: absolute;
    top: 578px;
    left: 0;
    right: 0;
    font-family: "Poppins", sans-serif;
    font-weight: 400;
    text-transform: uppercase;
    line-height: 1.1;
  }
  .venue .street { display: block; font-size: 23px; letter-spacing: 0.4px; }
  .venue .city { display: block; font-size: 45px; margin-top: 4px; letter-spacing: 1px; }
  .label {
    position: absolute;
    left: 0;
    right: 0;
    font-family: "Oswald", sans-serif;
    font-weight: 700;
    color: var(--orange);
    text-transform: uppercase;
    font-size: 34px;
    line-height: 1;
  }
  .label-tickets { top: 690px; }
  .label-seating { top: 810px; }
  .ticket-site {
    position: absolute;
    top: 740px;
    left: 0;
    right: 0;
    font-family: "Oswald", sans-serif;
    font-weight: 700;
    font-size: 52px;
    line-height: 1;
    text-transform: uppercase;
  }
  .prices {
    position: absolute;
    top: 856px;
    left: 0;
    right: 0;
    font-family: "Oswald", sans-serif;
    font-weight: 700;
    font-size: 56px;
    line-height: 1.03;
    text-transform: uppercase;
  }
  .prices span { display: block; }
  .band-photo {
    position: absolute;
    left: 26px;
    right: 26px;
    bottom: 26px;
    height: 210px;
    background: linear-gradient(180deg, rgba(15,15,15,0) 0%, #3a2a36 45%, #5a3e52 75%, #2a1f27 100%);
    z-index: 1;
  }
</style>
</head>
<body>
  <main class="poster">
    <div class="stage-backdrop" role="img" aria-label="Dark stage backdrop photo behind the event details"></div>
    <div class="notation-frame" role="img" aria-label="Faint border of musical notation symbols"></div>
    <div class="band-photo" role="img" aria-label="Photo of the ensemble performing on stage with saxophones and a microphone"></div>

    <div class="content">
      <div class="brand">tixolvo</div>

      <h1 class="title">
        <span class="line-1">HarmoNest</span>
        <span class="line-2">Ensemble</span>
        <span class="line-3">Jubilee</span>
      </h1>

      <div class="date-bar">Sunday Oct 2, 2022 When: 2-4 p.m.</div>

      <address class="venue" style="font-style: normal;">
        <span class="street">Brindle9 Alehouse, 413 Marlowe Ct #200</span>
        <span class="city">Sacramento, CA 95821</span>
      </address>

      <div class="label label-tickets">Tickets:</div>
      <div class="ticket-site">www.Tixolvo.com</div>

      <div class="label label-seating">General Seating:</div>
      <div class="prices">
        <span>$15 for adults &amp;</span>
        <span>$10 for students</span>
      </div>
    </div>
  </main>
</body>
</html>
```